Product name:Coral Reef Rum Punch

Type of product: Bottled Rum punch in flavors such as mango, passion fruit, melon and pina colada. It is delightful blend of Belvarine light rums which come in a variety of trpoical and natural flavors.

The bottle has an existing label design which is quite dated. Client wishes a new logo design. Must position the brand as premium and keep its Caribbean identity. Designers have the creative freedom to explore as many creative options as possible.

The challenge: for it to maintain its Caribbean identity but not look cliched with the generic Caribbean-type imagery as this has been done before. Though it is Caribbean born...it should also have an international look and feel to it.

```html
<!DOCTYPE html>
<html lang="en">
<head>
<meta charset="utf-8">
<title>Coral Reef Rum Punch – Label Range</title>
<link rel="stylesheet" href="https://fonts.googleapis.com/css2?family=Cinzel:wght@400;700;900&display=swap">
<style>
  :root {
    --canvas: #ffffff;
    --label-white: #f7f7f5;
    --ink-grey: #6b6b6b;
    --rule-grey: #9a9a9a;
    --name-cream: #fffbe6;
    --sun-yellow: #f4e21c;

    --melon-deep: #1f9a5c;
    --melon-mid: #7cc23a;
    --melon-fruit-a: #4f8f3a;
    --melon-fruit-b: #1f5d25;

    --mango-deep: #d8352a;
    --mango-mid: #f08a1e;
    --mango-fruit-a: #f5c33a;
    --mango-fruit-b: #e0452c;

    --pina-deep: #7a3a22;
    --pina-mid: #c0742a;
    --pina-fruit-a: #c99a2e;
    --pina-fruit-b: #4e7a2a;
  }

  * { box-sizing: border-box; margin: 0; padding: 0; }

  html, body {
    width: 1200px;
    height: 1126px;
    overflow: hidden;
    background: var(--canvas);
    font-family: "Cinzel", "Times New Roman", serif;
  }

  .label-range {
    position: relative;
    width: 1200px;
    height: 1126px;
    display: flex;
    justify-content: space-between;
    align-items: center;
    padding: 0 40px;
  }

  .label {
    width: 330px;
    display: flex;
    flex-direction: column;
    align-items: center;
    filter: drop-shadow(0 2px 4px rgba(0,0,0,0.12));
  }

  /* Brand crest */
  .brand-panel {
    position: relative;
    width: 100%;
    height: 190px;
    border-radius: 50% 50% 0 0 / 26% 26% 0 0;
    background: linear-gradient(to bottom, var(--sun-yellow) 0%, var(--tone-mid) 45%, var(--tone-deep) 100%);
    display: flex;
    flex-direction: column;
    align-items: center;
    justify-content: center;
    padding-top: 18px;
    color: var(--name-cream);
  }

  .brand-mark {
    position: absolute;
    top: -22px;
    left: 50%;
    width: 34px;
    height: 34px;
    margin-left: -17px;
    border-radius: 50%;
    background: var(--tone-mid);
    border: 3px solid var(--canvas);
  }

  .brand-name {
    font-weight: 700;
    font-size: 44px;
    line-height: 0.95;
    text-align: center;
    letter-spacing: -0.5px;
  }

  .brand-subline {
    margin-top: 10px;
    font-size: 13px;
    letter-spacing: 4px;
    font-weight: 400;
  }

  /* Flavour panel */
  .flavour-panel {
    width: 92%;
    background: var(--label-white);
    padding: 14px 16px 12px;
    display: flex;
    flex-direction: column;
    align-items: center;
  }

  .flavour-name {
    font-weight: 900;
    font-size: 34px;
    letter-spacing: 4px;
    color: var(--flavour-ink);
    line-height: 1;
  }

  .flavour-name.is-long { font-size: 27px; letter-spacing: 0; }

  .fruit-art {
    margin-top: 10px;
    width: 150px;
    height: 118px;
    border-radius: 50%;
    background: radial-gradient(circle at 40% 35%, var(--fruit-a), var(--fruit-b));
  }

  .serve-line {
    margin-top: 14px;
    width: 100%;
    display: flex;
    justify-content: space-between;
    font-size: 10px;
    color: var(--ink-grey);
    letter-spacing: 0.5px;
    border-bottom: 1px solid var(--rule-grey);
    padding-bottom: 3px;
  }

  .strength-line {
    margin-top: 6px;
    font-size: 9px;
    color: var(--ink-grey);
    word-spacing: 6px;
    text-transform: none;
    font-family: "Times New Roman", serif;
  }

  /* Descriptor band */
  .descriptor-band {
    width: 100%;
    height: 66px;
    border-radius: 10% 10% 10% 10% / 22% 22% 22% 22%;
    background: var(--tone-deep);
    color: var(--name-cream);
    display: flex;
    flex-direction: column;
    justify-content: center;
    align-items: center;
    font-size: 11px;
    letter-spacing: 3px;
    line-height: 1.6;
    text-align: center;
  }

  .label--melon {
    --tone-mid: var(--melon-mid);
    --tone-deep: var(--melon-deep);
    --flavour-ink: var(--melon-mid);
    --fruit-a: var(--melon-fruit-a);
    --fruit-b: var(--melon-fruit-b);
  }
  .label--mango {
    --tone-mid: var(--mango-mid);
    --tone-deep: var(--mango-deep);
    --flavour-ink: var(--mango-deep);
    --fruit-a: var(--mango-fruit-a);
    --fruit-b: var(--mango-fruit-b);
  }
  .label--pina {
    --tone-mid: var(--pina-mid);
    --tone-deep: var(--pina-deep);
    --flavour-ink: var(--pina-mid);
    --fruit-a: var(--pina-fruit-a);
    --fruit-b: var(--pina-fruit-b);
  }
</style>
</head>
<body>
<main class="label-range">

  <section class="label label--melon">
    <header class="brand-panel">
      <span class="brand-mark"></span>
      <h1 class="brand-name">CORAL<br>REEF</h1>
      <p class="brand-subline">• RUM PUNCH •</p>
    </header>
    <div class="flavour-panel">
      <h2 class="flavour-name">MELON</h2>
      <div class="fruit-art" role="img" aria-label="Illustration of a whole watermelon"></div>
      <p class="serve-line"><span>SERVE</span><span>OVER</span><span>CRUSHED</span><span>ICE</span></p>
      <p class="strength-line">17% alc/vol 750ml e</p>
    </div>
    <footer class="descriptor-band">
      <span>A BLEND OF CARIBBEAN RUM</span>
      <span>&amp; EXOTIC FRUIT FLAVOURS</span>
    </footer>
  </section>

  <section class="label label--mango">
    <header class="brand-panel">
      <span class="brand-mark"></span>
      <h1 class="brand-name">CORAL<br>REEF</h1>
      <p class="brand-subline">• RUM PUNCH •</p>
    </header>
    <div class="flavour-panel">
      <h2 class="flavour-name">MANGO</h2>
      <div class="fruit-art" role="img" aria-label="Illustration of a ripe mango with leaves"></div>
      <p class="serve-line"><span>SERVE</span><span>OVER</span><span>CRUSHED</span><span>ICE</span></p>
      <p class="strength-line">17% alc/vol 750ml e</p>
    </div>
    <footer class="descriptor-band">
      <span>A BLEND OF CARIBBEAN RUM</span>
      <span>&amp; EXOTIC FRUIT FLAVOURS</span>
    </footer>
  </section>

  <section class="label label--pina">
    <header class="brand-panel">
      <span class="brand-mark"></span>
      <h1 class="brand-name">CORAL<br>REEF</h1>
      <p class="brand-subline">• RUM PUNCH •</p>
    </header>
    <div class="flavour-panel">
      <h2 class="flavour-name is-long">PIÑA COLADA</h2>
      <div class="fruit-art" role="img" aria-label="Illustration of a pineapple with halved coconuts"></div>
      <p class="serve-line"><span>SERVE</span><span>OVER</span><span>CRUSHED</span><span>ICE</span></p>
      <p class="strength-line">17% alc/vol 750ml e</p>
    </div>
    <footer class="descriptor-band">
      <span>A BLEND OF CARIBBEAN RUM</span>
      <span>&amp; EXOTIC FRUIT FLAVOURS</span>
    </footer>
  </section>

</main>
</body>
</html>
```